Business Card Design Project

Crestline Vein Center

Dr Tomas Venrick M.D, F.R.C.S
Vascular and Vein Surgery

47-18 Pellham Avenue, Suite 314
Astoria
NY 11287

212-555-0147
718-555-0193
www.crestlinecare.us back of the card for scheduled appointments up to 5 appointment dates

Target Market(s)

Male and Female patients from 25 onwards with spider veins or varicose veins

Industry/Entity Type

Business

Font styles to use
Serif

Colors
86cae6
85abd2
0456a4

Requirements
Must have
• Modern Sophisticated design using light blue and grey text
Should not have
• hearts or flowers

```html
<!DOCTYPE html>
<html lang="en">
<head>
<meta charset="utf-8">
<title>Crestline Vein Center – Business Card</title>
<link rel="stylesheet" href="https://fonts.googleapis.com/css2?family=Playfair+Display:wght@700&family=PT+Sans:wght@400&display=swap">
<style>
  :root {
    --page: #f4f4f4;
    --card-white: #ffffff;
    --card-dark: #2a2a2c;
    --brand-blue: #0456a4;
    --mid-blue: #85abd2;
    --light-blue: #86cae6;
    --slot-fill: #f1f5fb;
    --text-light: #f2f2f2;
    --text-grey: #3a3a3a;
  }
  * { box-sizing: border-box; margin: 0; padding: 0; }
  html, body { width: 1200px; height: 900px; overflow: hidden; }
  body {
    background: var(--page);
    font-family: "PT Sans", sans-serif;
    position: relative;
  }
  .card {
    position: absolute;
    top: 295px;
    width: 540px;
    height: 310px;
    border-radius: 14px;
    overflow: hidden;
    box-shadow: 0 10px 24px rgba(0,0,0,0.18);
  }
  /* Front */
  .card-front { left: 40px; background: var(--card-dark); }
  .front-header {
    position: absolute; inset: 0 0 auto 0; height: 150px;
    background: var(--card-white);
  }
  .front-band {
    position: absolute; left: 0; right: 0; top: 150px; height: 9px;
    background: var(--brand-blue);
  }
  .brand-mark {
    position: absolute; left: 42px; top: 24px;
    width: 70px; height: 70px; border-radius: 50%;
    border: 3px solid var(--brand-blue);
  }
  .brand-name {
    position: absolute; left: 16px; top: 104px; width: 122px;
    text-align: center;
    font-size: 11px; color: var(--brand-blue);
  }
  .doctor {
    position: absolute; left: 150px; top: 56px;
  }
  .doctor-name {
    font-family: "Playfair Display", serif;
    font-weight: 700; font-size: 24px; color: var(--brand-blue);
    white-space: nowrap;
  }
  .doctor-name .credentials { font-size: 15px; }
  .doctor-specialty {
    font-size: 15px; color: var(--text-grey); margin-top: -2px;
  }
  .contact {
    position: absolute; left: 26px; top: 186px;
    list-style: none; color: var(--text-light); font-size: 14px;
  }
  .contact li { display: flex; align-items: flex-start; line-height: 20px; }
  .contact svg { width: 12px; height: 12px; margin: 4px 10px 0 0; flex: none; fill: var(--text-light); }
  .contact .no-icon { padding-left: 22px; }
  /* Back */
  .card-back { left: 620px; background: var(--card-dark); }
  .back-title {
    text-align: center; margin-top: 26px;
    font-size: 22px; color: var(--brand-blue);
  }
  .appointments {
    position: absolute; left: 50px; top: 76px;
    display: grid; grid-template-columns: 46px 210px 48px 104px;
    row-gap: 10px; align-items: end;
  }
  .slot-label { font-size: 15px; color: var(--brand-blue); padding-bottom: 2px; }
  .slot-label.time { padding-left: 8px; font-size: 14px; }
  .slot-box {
    height: 36px; background: var(--slot-fill);
    border: 2px solid var(--brand-blue);
  }
</style>
</head>
<body>
  <section class="card card-front" aria-label="Business card front">
    <div class="front-header"></div>
    <div class="front-band"></div>
    <div class="brand-mark" aria-hidden="true"></div>
    <div class="brand-name">Crestline Vein Center</div>
    <div class="doctor">
      <h1 class="doctor-name">Dr Tomas Venrick <span class="credentials">M.D, F.R.C.S</span></h1>
      <p class="doctor-specialty">vascular Surgery</p>
    </div>
    <ul class="contact">
      <li><svg viewBox="0 0 12 12"><path d="M6 0a4 4 0 0 0-4 4c0 3 4 8 4 8s4-5 4-8a4 4 0 0 0-4-4zm0 5.5A1.5 1.5 0 1 1 6 2.5a1.5 1.5 0 0 1 0 3z"/></svg>47-18 Pellham Avenue, Suite 314, Astoria, NY 11287</li>
      <li><svg viewBox="0 0 12 12"><path d="M1 4c0-2 2-3 5-3s5 1 5 3v1H8V3.5H4V5H1zM3 6h6l1.5 5h-9z"/></svg>212-555-0147</li>
      <li class="no-icon">718-555-0193</li>
      <li><svg viewBox="0 0 12 12"><path d="M6 0a6 6 0 1 0 0 12A6 6 0 0 0 6 0zm0 1c.8 0 1.6 1.8 1.8 4.5H4.2C4.4 2.8 5.2 1 6 1zM1 6.5h2.2c.1 1.5.4 2.8.9 3.7A5 5 0 0 1 1 6.5zm0-1a5 5 0 0 1 3.1-3.7c-.5.9-.8 2.2-.9 3.7zm5 5.5c-.8 0-1.6-1.8-1.8-4.5h3.6C7.6 9.2 6.8 11 6 11zm1.9-.8c.5-.9.8-2.2.9-3.7H11a5 5 0 0 1-3.1 3.7zM8.8 5.5c-.1-1.5-.4-2.8-.9-3.7A5 5 0 0 1 11 5.5z"/></svg>www.crestlinecare.us</li>
    </ul>
  </section>

  <section class="card card-back" aria-label="Business card back">
    <h2 class="back-title">Next Appointments</h2>
    <div class="appointments">
      <span class="slot-label">Date</span><span class="slot-box"></span><span class="slot-label time">Time</span><span class="slot-box"></span>
      <span class="slot-label">Date</span><span class="slot-box"></span><span class="slot-label time">Time</span><span class="slot-box"></span>
      <span class="slot-label">Date</span><span class="slot-box"></span><span class="slot-label time">Time</span><span class="slot-box"></span>
      <span class="slot-label">Date</span><span class="slot-box"></span><span class="slot-label time">Time</span><span class="slot-box"></span>
      <span class="slot-label">Date</span><span class="slot-box"></span><span class="slot-label time">Time</span><span class="slot-box"></span>
    </div>
  </section>
</body>
</html>
```